Institute for Hollow Relief at Annapolis
business card and stationary
Institute for Hollow Relief at Annapolis -
Creative Brief
Professional
Dominic T. Halloway, MD
472 Fenwick Court, Suite 208 Annapolis, MD 21409
dthalloway82@mailbright.example
www.wombrelief.example
Use new logo Comprehensive Gynecologic Care with Specialization in Chronic Pain Disorders and Minimally Invasive Surgery
Appointment Date and Time: Mon. _______ Tue _____ Wed ______ Thurs_______ Fri_______ _______ AM _______ PM

```html
<!DOCTYPE html>
<html lang="en">
<head>
<meta charset="utf-8">
<title>Institute for Hollow Relief at Annapolis — Business Card</title>
<link href="https://fonts.googleapis.com/css2?family=Cabin:wght@400;600;700&display=swap" rel="stylesheet">
<style>
  :root {
    --bg: #e9e7e4;
    --card: #ffffff;
    --plum: #a4569c;
    --plum-light: #c98fc2;
    --ink: #555555;
    --ink-soft: #8a8a8a;
    --rule: #d2d2d2;
    --swoosh: #6b6b6b;
  }
  * { margin: 0; padding: 0; box-sizing: border-box; }
  html, body {
    width: 1200px; height: 780px; overflow: hidden;
    background: var(--bg);
    font-family: "Cabin", "Gill Sans", sans-serif;
  }
  .card {
    position: absolute; left: 60px; top: 80px;
    width: 1080px; height: 620px;
    background: var(--card);
    border-radius: 26px;
    overflow: hidden;
    box-shadow: 0 10px 30px rgba(0,0,0,0.12);
  }
  .brand {
    position: absolute; left: 40px; top: 170px;
    width: 360px;
    display: flex; align-items: center; gap: 22px;
  }
  .brand-dot {
    flex: none; width: 78px; height: 78px; border-radius: 50%;
    background: var(--plum);
  }
  .brand-name {
    color: var(--ink);
    font-weight: 600;
    font-size: 27px;
    line-height: 1.12;
    text-transform: uppercase;
    letter-spacing: 0.5px;
  }
  .divider {
    position: absolute; left: 418px; top: 34px;
    width: 2px; height: 410px;
    background: var(--rule);
  }
  .contact {
    position: absolute; left: 458px; top: 50px;
    color: var(--ink);
  }
  .contact-name {
    color: var(--plum);
    font-weight: 700;
    font-size: 34px;
    letter-spacing: 0.3px;
  }
  .contact-address {
    margin-top: 58px;
    font-size: 21px;
    line-height: 1.45;
  }
  .contact-list {
    list-style: none;
    margin-top: 34px;
    font-size: 21px;
  }
  .contact-list li {
    display: flex; align-items: center; gap: 12px;
    height: 38px;
  }
  .contact-list svg { width: 20px; height: 20px; flex: none; }
  .band {
    position: absolute; left: 0; bottom: 0;
    width: 1080px; height: 200px;
  }
  .website {
    position: absolute; left: 0; right: 0; bottom: 38px;
    text-align: center;
    color: #ffffff;
    font-size: 22px;
    letter-spacing: 0.4px;
  }
</style>
</head>
<body>
  <main class="card">
    <div class="brand">
      <span class="brand-dot"></span>
      <span class="brand-name">Institute for Hollow Relief at Annapolis</span>
    </div>

    <div class="divider"></div>

    <section class="contact">
      <h1 class="contact-name">Dominic T. Halloway, MD</h1>
      <p class="contact-address">472 Fenwick Court, Suite 208<br>Annapolis, MD 21409</p>
      <ul class="contact-list">
        <li>
          <svg viewBox="0 0 20 20"><path d="M5 2 L8 2 L9 6 L7 8 Q9 12 12 13 L14 11 L18 12 L18 15 Q17 18 14 18 Q3 16 2 5 Q2 2 5 2 Z" fill="var(--plum)"/></svg>
          1-855-555-0148
        </li>
        <li>
          <svg viewBox="0 0 20 20"><path d="M5 2 L8 2 L9 6 L7 8 Q9 12 12 13 L14 11 L18 12 L18 15 Q17 18 14 18 Q3 16 2 5 Q2 2 5 2 Z" fill="var(--plum)"/></svg>
          410-555-0172
        </li>
        <li>
          <svg viewBox="0 0 20 20"><rect x="5" y="2" width="10" height="6" fill="var(--plum)"/><rect x="2" y="8" width="16" height="8" rx="2" fill="var(--plum)"/><rect x="5" y="13" width="10" height="5" fill="#fff" stroke="var(--plum)" stroke-width="1.5"/></svg>
          410-555-0193
        </li>
        <li>
          <svg viewBox="0 0 20 20"><circle cx="10" cy="10" r="8" fill="none" stroke="var(--plum)" stroke-width="2"/><circle cx="10" cy="10" r="3" fill="none" stroke="var(--plum)" stroke-width="2"/><path d="M13 8 L13 12 Q13 14 15 13" fill="none" stroke="var(--plum)" stroke-width="2"/></svg>
          dthalloway82@mailbright.example
        </li>
      </ul>
    </section>

    <svg class="band" viewBox="0 0 1080 200" preserveAspectRatio="none" aria-hidden="true">
      <path d="M0 110 Q520 150 1080 10 L1080 200 L0 200 Z" fill="var(--plum)"/>
      <path d="M0 104 Q520 146 1080 4" fill="none" stroke="var(--swoosh)" stroke-width="6"/>
      <path d="M0 118 Q540 158 1080 22" fill="none" stroke="var(--plum-light)" stroke-width="3" opacity="0.6"/>
    </svg>
    <p class="website">www.wombrelief.example</p>
  </main>
</body>
</html>
```